Industrial B2B Company Seeks Complete Redesign

We manufacture solid/liquid filtration equipment for manufacturers of chemicals, pharmaceuticals and mining products. We will be redesigning our website; our current design is outdated, and a more modern look is desired. Navigation can be improved. Call to action on the header, such as "Start Here". Video on home page. Designer should incorporate colors from our logo, at least the blues, the brown/gold is optional. Existing website can be found at www.BrindleSieves.com. Also, we do not make water filters and references to water or water-like images should be avoided.

```html
<!DOCTYPE html>
<html lang="en">
<head>
<meta charset="utf-8">
<title>Engineering Expertise at Your Service — BrindleSieves</title>
<link href="https://fonts.googleapis.com/css2?family=Inter:wght@400;500;700;800&display=swap" rel="stylesheet">
<style>
  :root {
    --navy: #17365a;
    --line: #1f3c5e;
    --bg: #ffffff;
    --glow: #eef1f5;
    --card-edge: #e6e8ec;
    --tile-light: #4a7bb0;
    --tile-mid: #24507e;
    --tile-dark: #17355a;
    --on-tile: #ffffff;
  }
  * { box-sizing: border-box; margin: 0; padding: 0; }
  html, body {
    width: 1200px; height: 576px; overflow: hidden;
    background: var(--bg);
    font-family: "Inter", Arial, sans-serif;
    color: var(--navy);
  }
  .section {
    position: relative; width: 1200px; height: 576px;
    border: 1px solid var(--card-edge); border-radius: 8px;
    background: radial-gradient(ellipse 520px 130px at 595px 60px, var(--glow), var(--bg) 100%);
    overflow: hidden;
  }
  .section-title {
    position: absolute; top: 42px; left: 0; width: 1190px;
    text-align: center; font-weight: 800; font-size: 49px;
    line-height: 65px; letter-spacing: 0.3px;
  }
  .rule { position: absolute; background: var(--line); }
  .rule-h { left: 162px; top: 383px; width: 876px; height: 1.5px; }
  .rule-v { width: 1.5px; }
  .highlight-tile {
    position: absolute; left: 380px; top: 235px; width: 220px; height: 149px;
    background: radial-gradient(ellipse 170px 140px at 70px 35px, var(--tile-light), var(--tile-mid) 55%, var(--tile-dark) 100%);
  }
  .feature {
    position: absolute; width: 219px; text-align: center;
  }
  .feature-heading {
    font-weight: 500; font-size: 25px; line-height: 25px;
  }
  .feature-text {
    margin-top: 15px; font-size: 15.5px; line-height: 25px;
  }
  .feature-stat .feature-heading { font-size: 27px; line-height: 28px; }
  .feature-stat .feature-text { margin-top: 13px; }
  .feature-highlight { color: var(--on-tile); }
</style>
</head>
<body>
<section class="section">
  <h1 class="section-title">ENGINEERING EXPERTISE<br>AT YOUR SERVICE</h1>

  <div class="highlight-tile"></div>

  <div class="rule rule-h"></div>
  <div class="rule rule-v" style="left:819px;top:237px;height:293px"></div>
  <div class="rule rule-v" style="left:379px;top:384px;height:146px"></div>
  <div class="rule rule-v" style="left:599px;top:384px;height:146px"></div>

  <div class="feature feature-stat" style="left:161px;top:266px">
    <div class="feature-heading">~100 years</div>
    <div class="feature-text" style="padding-left:16px">unparalleled history<br>of expertise</div>
  </div>
  <div class="feature feature-highlight" style="left:380px;top:246px">
    <div class="feature-heading">Engineering<br>Expertise</div>
    <div class="feature-text">in industrial<br>liquid filtration</div>
  </div>
  <div class="feature" style="left:600px;top:246px">
    <div class="feature-heading">Best<br>Solutions</div>
    <div class="feature-text">for your<br>unique challenges</div>
  </div>
  <div class="feature" style="left:820px;top:246px">
    <div class="feature-heading">Customized<br>Approach</div>
    <div class="feature-text">Brindle works closely<br>with you</div>
  </div>

  <div class="feature" style="left:161px;top:406px">
    <div class="feature-heading">Optimal<br>Solutions</div>
    <div class="feature-text">developed for<br>your needs</div>
  </div>
  <div class="feature" style="left:380px;top:406px">
    <div class="feature-heading">Application<br>Goals</div>
    <div class="feature-text">tailored solutions<br>for all applications</div>
  </div>
  <div class="feature" style="left:600px;top:406px">
    <div class="feature-heading">Dedicated<br>Support</div>
    <div class="feature-text">ready to deliver<br>the best results</div>
  </div>
  <div class="feature" style="left:826px;top:418px">
    <div class="feature-heading">Commitment</div>
    <div class="feature-text" style="margin-top:22px;margin-left:-6px">to your success<br>and satisfaction</div>
  </div>
</section>
</body>
</html>
```